Word Page Templates x 5

1 x Letterhead Template with Header and Footer able to be printed to paper and pdf with non blurry resolution
- File attached looks ok on computer screen but does not print the same
- We are wanting it to print like it looks on the screen
- We are wanting it to print not fuzzy in resolution
- We are wanting the banner to be on the absolute edge of the page like it is on the computer screen
- We are needing to print this to paper and pdf with perfect resolution and colour

Please can someone help us!!

I have provided the logo files in our posession. If better resolutions are required please let us know.

We are also wanting 4 simple page templates to be setup in Landscape and Portrait orientation as well once we are happy with the letterhead that is provided samples have been provided
Updates

Hi all I have the vector files available now along with a Colour profile

Requirements
Must have
• Clear when printed on A4 Paper
Should not have
• Blurry images, Colour must be correct (same as Logo) - Please reference our website if need be ..... vornal.com.au

```html
<!DOCTYPE html>
<html lang="en">
<head>
<meta charset="utf-8">
<title>Vornal Pavement Services – Letterhead</title>
<link href="https://fonts.googleapis.com/css2?family=Roboto:wght@400;500;700;900&display=swap" rel="stylesheet">
<style>
  :root {
    --brand-green: #1e8a3c;
    --brand-navy: #27307a;
    --brand-blue: #2e3d95;
    --text-body: #3c3c3c;
    --text-grey: #6d6d6d;
    --badge-grey: #b9b9b9;
    --backdrop: #3a3735;
    --paper: #ffffff;
  }
  * { margin: 0; padding: 0; box-sizing: border-box; }
  html, body {
    width: 1200px; height: 822px; overflow: hidden;
    background: var(--backdrop);
    font-family: "Roboto", Arial, sans-serif;
  }
  .letterhead {
    position: absolute; left: 320px; top: 16px;
    width: 559px; height: 790px;
    background: var(--paper);
  }
  .edge-band {
    position: absolute; left: 0; width: 100%; height: 23px;
    background: linear-gradient(90deg, var(--brand-green) 0%, #1f7a78 50%, var(--brand-blue) 100%);
  }
  .edge-band.top { top: 0; }
  .edge-band.bottom { bottom: 0; }

  .brand { position: absolute; left: 33px; top: 44px; width: 200px; }
  .brand-name {
    font-weight: 900; font-size: 46px; letter-spacing: 1px;
    color: var(--brand-green); line-height: 46px;
  }
  .brand-tagline {
    font-size: 11.5px; font-weight: 500; letter-spacing: 1.2px;
    color: var(--text-grey); text-align: right; margin-top: 2px;
  }

  .contact-list { position: absolute; left: 370px; top: 51px; list-style: none; }
  .contact-list li {
    display: flex; align-items: center; gap: 7px;
    font-size: 9.4px; color: var(--brand-navy); height: 11.6px;
  }
  .contact-list svg { width: 10px; height: 10px; flex: none; }

  .letter-title {
    position: absolute; left: 38px; top: 168px;
    font-size: 20px; font-weight: 400; color: var(--brand-navy);
  }
  .letter-body {
    position: absolute; left: 38px; top: 204px; width: 489px;
    font-size: 10.2px; line-height: 14.1px; color: var(--text-body);
    text-align: justify;
  }
  .letter-body p { margin-bottom: 14.1px; }

  .signature {
    position: absolute; left: 40px; top: 600px; width: 80px; height: 16px;
    background: linear-gradient(90deg, #d6d6d6, #eeeeee);
    border-radius: 3px;
  }

  .footer-rule { position: absolute; top: 684px; height: 3px; }
  .footer-rule.navy { left: 38px; width: 355px; background: var(--brand-navy); }
  .footer-rule.green { left: 416px; width: 110px; background: var(--brand-green); }
  .affiliation-note {
    position: absolute; left: 39px; top: 697px;
    font-size: 7.8px; font-weight: 700; color: var(--brand-navy);
  }
  .affiliate-badges { position: absolute; left: 33px; top: 712px; display: flex; gap: 22px; align-items: center; }
  .badge { height: 38px; background: var(--badge-grey); border-radius: 3px; }
  .badge.wide { width: 100px; background: var(--brand-navy); opacity: .85; }
  .badge.small { width: 46px; }
  .badge.round { width: 40px; border-radius: 50%; }

  .footer-brand { position: absolute; left: 426px; top: 722px; text-align: right; width: 100px; }
  .footer-brand .brand-name { font-size: 25px; line-height: 25px; letter-spacing: .5px; }
  .footer-brand .brand-tagline { font-size: 6px; letter-spacing: .6px; margin-top: 1px; }
</style>
</head>
<body>
<main class="letterhead">
  <div class="edge-band top" role="img" aria-label="Chevron pattern band in green to blue"></div>

  <header>
    <div class="brand">
      <div class="brand-name">VORNAL</div>
      <div class="brand-tagline">PAVEMENT SERVICES</div>
    </div>
    <ul class="contact-list">
      <li><svg viewBox="0 0 10 10"><circle cx="5" cy="5" r="5" fill="#1e8a3c"/><path d="M3.3 2.6l1 1-.5.7c.3.7.8 1.2 1.5 1.5l.7-.5 1 1-.6.8C4.8 7 3 5.2 2.9 3.2z" fill="#fff"/></svg>07 5550 0142</li>
      <li><svg viewBox="0 0 10 10"><circle cx="5" cy="5" r="5" fill="#1e8a3c"/><rect x="2.6" y="3.3" width="4.8" height="3.4" fill="none" stroke="#fff" stroke-width=".8"/><path d="M2.6 3.3L5 5.2l2.4-1.9" fill="none" stroke="#fff" stroke-width=".8"/></svg>admin@vornal.com.au</li>
      <li><svg viewBox="0 0 10 10"><circle cx="5" cy="5" r="5" fill="#1e8a3c"/><circle cx="5" cy="5" r="2.6" fill="none" stroke="#fff" stroke-width=".7"/><path d="M2.4 5h5.2M5 2.4v5.2" stroke="#fff" stroke-width=".6"/></svg>www.vornal.com.au</li>
      <li><svg viewBox="0 0 10 10"><circle cx="5" cy="5" r="5" fill="#1e8a3c"/><path d="M5 2.3a1.9 1.9 0 0 1 1.9 1.9C6.9 5.6 5 7.7 5 7.7S3.1 5.6 3.1 4.2A1.9 1.9 0 0 1 5 2.3z" fill="#fff"/></svg>PO Box 2210, Marlow QLD 4230</li>
    </ul>
  </header>

  <h1 class="letter-title">Business Proposals</h1>
  <section class="letter-body">
    <p>Lorem ipsum dolor sit amet, consectetur adipiscing elit. Etiam sit amet nisi sit amet nibh dignis sim elementum id suscipit leo. Sed ut condimentum diam. Sed ac nulla libero. Morbi ante ante inte rdum luctus dictum ut, sollicitudin in mi. Donec aliquet lectus quis enim tempor ullamcorper pelle ntesque et neque posuere, gravida lacus molestie, pretium ex. Vivamus in justo ac ante lacinia pharetra.</p>
    <p>Donec ultrices lacinia arcu, eget faucibus quam rhoncus id. Sed convallis eros neque, quis effici tur erat euismod vel. Mauris consequat nunc quis tortor efficitur euismod. Curabitur posuere hendrerit semper nam dignissim sed tellus id fermentum.</p>
    <p>Phasellus id dui arcu nullam finibus nisl quis quam egestas blandit. Praesent eu leo justo nullam porta nisi non tempus lacinia. Quisque molestie nulla id volutpat congue.</p>
    <p>Proin gravida nibh vel velit auctor aliquet. Aenean sollicitudin, lorem quis bibendum auctor, nisi elit consequat ipsum, nec sagittis sem nibh id elit. Duis sed odio sit amet nibh vulputate cursus a sit amet mauris. Morbi accumsan ipsum velit. Nam nec tellus a odio tincidunt auctor a ornare odio. Sed non mauris vitae erat consequat auctor eu in elit. Class aptent taciti sociosqu ad litora torquent per conubia nostra, per inceptos himenaeos. Mauris in erat justo. Nullam ac urna eu felis dapibus condimentum sit amet a augue. Sed non neque elit. Sed ut imperdiet nisi. Proin condimentum fermentum nunc. Etiam pharetra, erat sed fermentum feugiat, velit mauris egestas quam, ut aliquam massa nisl quis neque. Suspendisse in orci enim. Donec ultrices lacinia arcu, eget faucibus quam rhoncus id. Sed convallis eros neque, quis effici tur erat euismod vel. Mauris consequat nunc quis tortor efficitur euismod. Curabitur posuere hendrerit semper nam dignissim sed tellus id fermentum.</p>
    <p>Donec ultrices lacinia arcu, eget faucibus quam rhoncus id. Sed convallis eros neque, quis effici tur erat euismod vel. Mauris consequat nunc quis tortor efficitur euismod. Curabitur posuere hendrerit semper nam dignissim sed tellus id fermentum.</p>
  </section>
  <div class="signature" role="img" aria-label="Handwritten signature"></div>

  <footer>
    <div class="footer-rule navy"></div>
    <div class="footer-rule green"></div>
    <div class="affiliation-note">VORNAL PAVEMENT SERVICES ARE PROUDLY AFFILIATED WITH</div>
    <div class="affiliate-badges">
      <div class="badge wide" role="img" aria-label="Affiliate badge"></div>
      <div class="badge small" role="img" aria-label="Affiliate badge"></div>
      <div class="badge small" role="img" aria-label="Member badge"></div>
      <div class="badge round" role="img" aria-label="Association badge"></div>
    </div>
    <div class="footer-brand">
      <div class="brand-name">VORNAL</div>
      <div class="brand-tagline">PAVEMENT SERVICES</div>
    </div>
  </footer>

  <div class="edge-band bottom" role="img" aria-label="Chevron pattern band in green to blue"></div>
</main>
</body>
</html>
```